Build Steady Practice Growth Through Trust

Design a cover for this book which is designed to help a business go from it's current revenue and treatment acceptance to double (2X) that success and those metrics.

```html
<!DOCTYPE html>
<html lang="en">
<head>
<meta charset="utf-8">
<title>Book Cover – 2X Your Revenue</title>
<link rel="stylesheet" href="https://fonts.googleapis.com/css2?family=Oswald:wght@500;600;700&display=swap">
<style>
  :root {
    --cover-red: #b81f26;
    --numeral-cream: #fdfaf7;
    --ink-black: #060708;
    --revenue-blue: #0094d8;
    --page-white: #ffffff;
    --text-white: #ffffff;
    --art-green: #8cc75a;
    --art-skin: #f1d0c4;
    --art-navy: #3a3797;
  }
  html, body {
    margin: 0;
    padding: 0;
    width: 1126px;
    height: 1200px;
    overflow: hidden;
    background: var(--page-white);
  }
  .cover-canvas {
    display: block;
    width: 1126px;
    height: 1200px;
  }
  .cover-board { fill: var(--cover-red); }
  .numeral-backdrop { fill: var(--numeral-cream); }
  .numeral-counter { fill: var(--cover-red); }
  .tagline {
    font-family: "Oswald", sans-serif;
    font-weight: 600;
    font-variant: small-caps;
    fill: var(--text-white);
  }
  .title-multiplier {
    font-family: "Oswald", sans-serif;
    font-weight: 700;
    fill: var(--cover-red);
  }
  .title-your {
    font-family: "Oswald", sans-serif;
    font-weight: 700;
    fill: var(--ink-black);
  }
  .title-revenue {
    font-family: "Oswald", sans-serif;
    font-weight: 600;
    fill: var(--revenue-blue);
  }
  .author-name {
    font-family: "Oswald", sans-serif;
    font-weight: 600;
    fill: var(--text-white);
  }
</style>
</head>
<body>
<svg class="cover-canvas" viewBox="0 0 1866 1988" xmlns="http://www.w3.org/2000/svg">
  <defs>
    <linearGradient id="art-tones" x1="0" y1="0" x2="0" y2="1">
      <stop offset="0" stop-color="var(--art-green)"/>
      <stop offset="0.55" stop-color="var(--art-green)"/>
      <stop offset="0.75" stop-color="var(--art-skin)"/>
      <stop offset="1" stop-color="var(--art-navy)"/>
    </linearGradient>
  </defs>

  <rect class="cover-board" x="357" y="126" width="1149" height="1736"/>

  <text class="tagline" x="447" y="288" font-size="50" textLength="971" lengthAdjust="spacingAndGlyphs">Build Steady Practice Growth Through Trust</text>

  <g class="big-numeral">
    <path class="numeral-backdrop" d="M445,812 L445,660 C445,510 520,428 655,428 L966,428 L1094,611 L1220,428 L1418,428 L1380,610 C1350,760 1342,870 1342,990 C1342,1120 1352,1230 1380,1370 L1418,1561 L1220,1561 L1094,1368 L966,1561 L445,1561 Z"/>
    <path class="numeral-counter" d="M445,812 L594,812 L594,1055 C520,1110 445,1200 445,1330 Z"/>
    <path class="numeral-counter" d="M594,812 L594,660 C594,610 615,587 659,587 C703,587 724,610 724,660 L724,860 C800,880 905,900 905,990 C905,1130 875,1240 833,1402 L594,1402 L594,1330 C594,1230 670,1160 760,1080 C700,1000 640,920 594,880 Z"/>
  </g>

  <rect class="money-hand-art" role="img" aria-label="Illustration of a hand in a blue suit sleeve holding up two green dollar bills" x="540" y="720" width="380" height="682" rx="14" fill="url(#art-tones)"/>

  <g class="book-title">
    <text class="title-multiplier" x="928" y="972" font-size="380" textLength="385" lengthAdjust="spacingAndGlyphs">2X</text>
    <text class="title-your" x="928" y="1168" font-size="222" textLength="395" lengthAdjust="spacingAndGlyphs">YOUR</text>
    <text class="title-revenue" x="931" y="1302" font-size="132" textLength="393" lengthAdjust="spacingAndGlyphs">REVENUE</text>
  </g>

  <text class="author-name" x="625" y="1757" font-size="84" textLength="615" lengthAdjust="spacing">WRITTER NAME</text>
</svg>
</body>
</html>
```